Flyer für Freie Referentin
I thank Merak Tuwero for the great work! I’am very satisfied with the design of my flyer, with the arrangement of the photos, the font and the colors. Everything is fine and exactly as I imagined before. All my requested changings were changed very quickly and correctly. I would definitely recommend this designer!
Zielgruppe
Ich biete Vorträge, Kurse, Fortbildungen und Privatunterricht an zu den Themen:
Einführung in die Weltreligionen
und
Feste der Religionen
Außerdem biete ich Führungen durch religiöse Gebäude in Berlin an.
Meine Zielgruppen sind:
1. Pädagogen in Kita, Grund-und Oberschule,
2. Religionslehrer,
3.Fachkräfte im interkulturellen Kontext (Ausländerbehörde, Gesundheitswesen, Sozialwesen) und
4. Menschen, die gern reisen und sich für andere Religionen und Kulturen interessieren
Aufgabenstellung
Ich habe selbst einen 6 seitigen Falzflyer entworfen, mit Text und Bildern und würde diesen inhaltlich weitgehend so lassen, und nur in einem ansprechenden Design umgestalten lassen. Die Fotos, die ich liefere, habe ich in den religiösen Gebäuden selbst gemacht.

```html
<!DOCTYPE html>
<html lang="de">
<head>
<meta charset="utf-8">
<title>Flyer Weltreligionen in Berlin erleben</title>
<link href="https://fonts.googleapis.com/css2?family=Cinzel:wght@600;700&family=Poppins:ital,wght@0,400;0,500;0,600;0,700;1,400&display=swap" rel="stylesheet">
<style>
:root{
  --red:#8e1b22;
  --red-dark:#6a0f19;
  --maroon:#5a0b1c;
  --gold:#f2c230;
  --gold-soft:#d8b54a;
  --black:#141414;
  --paper:#efece7;
  --grey:#dcd9d5;
  --ink:#1d1d1d;
  --bg:#d3d3d3;
}
*{box-sizing:border-box;margin:0;padding:0}
html,body{width:706px;height:1200px;overflow:hidden}
body{background:var(--bg);font-family:"Poppins",sans-serif;color:var(--ink);position:relative}
.spread{position:absolute;left:13px;width:680px;height:500px;display:flex;box-shadow:0 8px 22px rgba(0,0,0,.25)}
.spread--outside{top:55px}
.spread--inside{top:635px}
.panel{width:33.333%;height:100%;position:relative;overflow:hidden;display:flex;flex-direction:column}
.serif{font-family:"Cinzel",serif;font-weight:700;letter-spacing:.3px}
.rule{height:1.5px;margin:5px 12px 8px}
.ticks{list-style:none}
.ticks li{position:relative;padding-left:14px;margin-bottom:7px;line-height:1.3}
.ticks li::before{content:"";position:absolute;left:1px;top:2px;width:7px;height:4px;border-left:2px solid var(--tick,var(--gold));border-bottom:2px solid var(--tick,var(--gold));transform:rotate(-45deg)}
.photo{border-radius:0}

/* Outside - about */
.about{background:linear-gradient(180deg,var(--black) 0 37%,var(--red) 37% 100%)}
.about__title{color:var(--gold);text-align:center;font-size:12px;margin-top:34px}
.about .rule{background:#fff;margin:4px 14px 10px}
.about__portrait{margin:0 auto;width:150px;height:170px;border:3px solid var(--gold);background:linear-gradient(160deg,#f6b021,#e79312)}
.about__name{color:#fff;font-size:16px;text-align:center;margin:20px 0 10px}
.about .ticks{color:#fff;font-size:7.4px;padding:0 20px 0 26px}
.about .ticks li{margin-bottom:10px}

/* Outside - contact */
.contact{background:var(--paper);padding:0 12px}
.contact__title{color:var(--red);text-align:center;font-size:12px;margin-top:34px}
.contact .rule{background:var(--red);margin:4px 0 8px}
.contact__name{color:var(--red);font-size:16px;text-align:center}
.contact__role{color:var(--red);font-style:italic;font-size:7px;text-align:center;margin-bottom:8px}
.contact__list{list-style:none;padding-left:14px}
.contact__list li{display:flex;align-items:flex-start;gap:7px;font-size:10px;font-weight:500;line-height:1.2;margin-bottom:4px}
.contact__list svg{flex:0 0 10px;margin-top:2px}
.contact__symbols{width:90px;height:78px;margin:8px auto 10px;background:radial-gradient(circle,#d9d5cf,#e9e6e1);border-radius:6px}
.booking{border:2px solid var(--red);background:#fff;padding:6px 7px 8px;font-size:7px;line-height:1.3}
.booking__head{background:var(--red);color:#fff;text-align:center;font-size:10px;padding:3px 0;margin-bottom:6px}
.booking p{margin-bottom:6px}
.booking .ticks{--tick:var(--red)}
.booking .ticks li{margin-bottom:5px}

/* Outside - cover */
.cover{background:var(--maroon)}
.cover__title{color:#fff;text-align:center;font-size:15px;line-height:1.05;margin-top:30px}
.tag{background:var(--gold-soft);color:var(--black);font-weight:600;font-size:8px;text-align:center;margin:0 auto;padding:2px 7px}
.tag--first{margin-top:10px;margin-bottom:4px}
.cover__grid{display:grid;grid-template-columns:1fr 1fr;grid-template-rows:1fr 1fr;gap:3px;height:150px;margin:10px 0 0 14px}
.cover__bands{margin-top:auto}
.cover__faiths{background:var(--gold-soft);color:var(--black);font-weight:700;font-size:10px;text-align:center;line-height:1.25;padding:9px 6px}
.cover__slogan{background:var(--black);color:#fff;text-align:center;font-size:11px;line-height:1.25;padding:16px 8px 22px}

/* Inside - offer */
.offer__top{background:var(--red);padding:20px 14px 10px;height:232px}
.offer__title{color:var(--gold);text-align:center;font-size:11px;line-height:1.05}
.offer__top .rule{background:#fff;margin:7px 0 10px}
.offer__top .ticks{color:#fff;font-size:7.6px;padding-left:12px}
.offer__themes{background:var(--grey);padding:12px 14px 6px;height:152px}
.offer__themes-title{color:var(--red);font-size:10.5px;text-align:center}
.offer__themes .rule{background:var(--red);margin:4px 0 7px}
.theme{margin-left:8px;margin-bottom:5px}
.theme__head{display:flex;align-items:center;gap:6px;color:var(--red);font-family:"Cinzel",serif;font-weight:700;font-size:7.5px;margin-bottom:2px}
.num{width:11px;height:11px;border-radius:50%;background:var(--red);color:#fff;font-family:"Poppins",sans-serif;font-size:7px;display:flex;align-items:center;justify-content:center;flex:0 0 11px}
.theme .ticks{--tick:var(--red);font-size:7.3px;padding-left:14px}
.theme .ticks li{margin-bottom:0}
.offer__photo{flex:1;background:linear-gradient(120deg,#2f7d2c,#8a3b12 55%,#e07b16)}

/* Inside - visits */
.visits{background:linear-gradient(180deg,var(--red) 0 50%,var(--black) 50% 100%)}
.visits__title{color:var(--gold);text-align:center;font-size:10.5px;margin-top:20px}
.visits .rule{background:#fff;margin:5px 14px 8px}
.visits .ticks{color:#fff;font-size:8px;padding-left:30px}
.visits .ticks li{margin-bottom:2px}
.visits__photo{margin:10px auto 0;width:200px;height:200px;border:3px solid var(--gold);background:linear-gradient(150deg,#556b3a,#b8713c 45%,#c23a6a 75%,#6b3b2a)}
.visits__take{color:var(--gold);text-align:center;font-size:10.5px;margin-top:26px}
.visits .ticks--take{font-size:7.4px;padding:0 18px 0 30px}
.visits .ticks--take li{margin-bottom:9px}

/* Inside - audience */
.audience{background:var(--paper)}
.audience__photo{height:172px;background:linear-gradient(180deg,#3f78c8,#9bbde6 60%,#c9c6be)}
.audience__title{color:var(--red);text-align:center;font-size:11px;line-height:1.05;margin-top:14px}
.audience .rule{background:var(--red);margin:6px 14px 8px}
.group{padding:0 12px 0 18px;margin-bottom:7px}
.group .theme__head{font-size:7px;align-items:flex-start;line-height:1.15}
.group .ticks{--tick:var(--red);font-size:7.2px;padding-left:17px}
.group .ticks li{margin-bottom:0}
.audience__foot{margin-top:auto;height:7px;background:var(--black)}
</style>
</head>
<body>

<section class="spread spread--outside" aria-label="Flyer Außenseite">
  <div class="panel about">
    <h2 class="about__title serif">Über mich:</h2>
    <div class="rule"></div>
    <div class="about__portrait photo" role="img" aria-label="Porträtfoto der Referentin vor orangem Hintergrund"></div>
    <h3 class="about__name serif">Dr. Carla Hennig</h3>
    <ul class="ticks">
      <li>1992-1999 Studium der Religionswissenschaft und Indologie inBerlin</li>
      <li>2008 Dissertation: „Hindus in der deutschen Diaspora.“</li>
      <li>eit 2000 Wissenschaftliche Referentin für Weltreligionen und Hinduismus</li>
      <li>Seit 2002 Freie Autorin, Schwerpunkt: Religiöse Gruppen in der Diaspora</li>
    </ul>
  </div>

  <div class="panel contact">
    <h2 class="contact__title serif">Kontakt</h2>
    <div class="rule"></div>
    <h3 class="contact__name serif">Dr. Carla Hennig</h3>
    <p class="contact__role">Religionswissenschaftlerin und Indologin</p>
    <ul class="contact__list">
      <li><svg width="10" height="11" viewBox="0 0 10 12"><path d="M5 0a4 4 0 0 1 4 4c0 3-4 8-4 8S1 7 1 4a4 4 0 0 1 4-4z" fill="#8e1b22"/><circle cx="5" cy="4" r="1.5" fill="#fff"/></svg><span>Lindenhofweg 7<br>10115 Berlin</span></li>
      <li><svg width="10" height="10" viewBox="0 0 10 10"><circle cx="5" cy="5" r="5" fill="#8e1b22"/><path d="M3 3l1 0 .6 1.3-.6.6c.4.8.9 1.3 1.6 1.6l.6-.6L7.5 6.5v1C5 8 2.5 5.5 3 3z" fill="#fff"/></svg><span>030 55501234</span></li>
      <li><svg width="10" height="11" viewBox="0 0 10 12"><rect x="2" y="0.5" width="6" height="11" rx="1" fill="none" stroke="#8e1b22" stroke-width="1.3"/><circle cx="5" cy="9.5" r=".7" fill="#8e1b22"/></svg><span>017655501239</span></li>
      <li><svg width="10" height="10" viewBox="0 0 10 10"><circle cx="5" cy="5" r="5" fill="#8e1b22"/><rect x="2.5" y="3.2" width="5" height="3.6" fill="none" stroke="#fff" stroke-width=".8"/><path d="M2.5 3.2L5 5.3 7.5 3.2" fill="none" stroke="#fff" stroke-width=".8"/></svg><span>info@fermoxabbe.de</span></li>
      <li><svg width="10" height="10" viewBox="0 0 10 10"><circle cx="5" cy="5" r="5" fill="#8e1b22"/><circle cx="5" cy="5" r="3" fill="none" stroke="#fff" stroke-width=".7"/><path d="M2 5h6M5 2v6" stroke="#fff" stroke-width=".7"/></svg><span>www.fermoxabbe.de</span></li>
    </ul>
    <div class="contact__symbols" role="img" aria-label="Gruppe religiöser Symbole der fünf Weltreligionen"></div>
    <div class="booking">
      <h3 class="booking__head serif">Mehr Infos &amp; Buchung</h3>
      <p>Ich biete Seminare für Einzelpersonen, Bildungseinrichtungen und Teams an – in meinem Büro oder vor Ort.</p>
      <ul class="ticks">
        <li>Aktuelle Preise und Konditionen finden Sie auf meiner Website www.fermoxabbe.de</li>
        <li>Individuelle Angebote – Preise auf Nachfrage unter: info@fermoxabbe.de oder: Tel.: 03(0) 555 01234</li>
      </ul>
    </div>
  </div>

  <div class="panel cover">
    <h1 class="cover__title serif">Weltreligionen in<br>Berlin erleben</h1>
    <p class="tag tag--first">VORTRÄGE &amp; SEMINARE</p>
    <p class="tag">FÜHRUNGEN &amp; PRIVATUNTERRICHT<br>IN BERLIN</p>
    <div class="cover__grid">
      <div class="photo" role="img" aria-label="Foto aus einer Synagoge" style="background:linear-gradient(135deg,#2c2c34,#8d8a86)"></div>
      <div class="photo" role="img" aria-label="Foto einer Feier in einem Tempel" style="background:linear-gradient(135deg,#b0456a,#2b8a86)"></div>
      <div class="photo" role="img" aria-label="Foto buddhistischer Mönche" style="background:linear-gradient(135deg,#b47f4b,#e08a1a)"></div>
      <div class="photo" role="img" aria-label="Foto eines orthodoxen Festgottesdienstes" style="background:linear-gradient(135deg,#c9c2b8,#6b4a3a)"></div>
    </div>
    <div class="cover__bands">
      <p class="cover__faiths">JUDENTUM | CHRISTENTUM |<br>ISLAM | HINDUISMUS |<br>BUDDHISMUS</p>
      <p class="cover__slogan serif">Lernen Sie die<br>Weltreligionen kennen<br>undverstehen!</p>
    </div>
  </div>
</section>

<section class="spread spread--inside" aria-label="Flyer Innenseite">
  <div class="panel offer">
    <div class="offer__top">
      <h2 class="offer__title serif">Weltreligionen verstehen –Menschen besser begegnen Mein Angebot:</h2>
      <div class="rule"></div>
      <ul class="ticks">
        <li>Vorträge &amp; Seminare zu: Judentum, Christentum, Islam, Hinduismus und Buddhismus</li>
        <li>Vorträge &amp; Seminare zu religiösen Festen und Traditionen</li>
        <li>Besuche religiöser Stätten</li>
        <li>Individuelle Weiterbildungen &amp; Privatunterricht</li>
      </ul>
    </div>
    <div class="offer__themes">
      <h2 class="offer__themes-title serif">Welche Themen biete ich an?</h2>
      <div class="rule"></div>
      <div class="theme">
        <p class="theme__head"><span class="num">1</span>Einführung Weltreligionen</p>
        <ul class="ticks"><li>erkunft &amp; HeiligeSchrift</li><li>Lehren &amp; Rituale</li><li>Ethik &amp; Verhalten</li></ul>
      </div>
      <div class="theme">
        <p class="theme__head"><span class="num">2</span>Este in den Religionen</p>
        <ul class="ticks"><li>Kalender &amp; Anlässe</li><li>Geschichten &amp; Musik</li><li>Rituale &amp; Speisen</li></ul>
      </div>
    </div>
    <div class="offer__photo photo" role="img" aria-label="Foto einer Tonschale mit Opferfeuer vor grünem Gewand"></div>
  </div>

  <div class="panel visits">
    <h2 class="visits__title serif">Besuche religiöser Stätten</h2>
    <div class="rule"></div>
    <ul class="ticks">
      <li>Führung durch die Räume</li>
      <li>Teilnahme an Zeremonien</li>
      <li>Austausch mit Gläubigen</li>
    </ul>
    <div class="visits__photo photo" role="img" aria-label="Foto einer farbenfrohen hinduistischen Prozession auf der Straße"></div>
    <h2 class="visits__take serif">Was Sie mitnehmen:</h2>
    <div class="rule"></div>
    <ul class="ticks ticks--take">
      <li>Klar verständliches Wissen zu den Weltreligionen</li>
      <li>Hintergründe zu Festen, Bräuchen und Symbolen</li>
      <li>Aha-Momente für Beruf, Alltag und Reisen</li>
    </ul>
  </div>

  <div class="panel audience">
    <div class="audience__photo photo" role="img" aria-label="Foto einer Moschee mit zwei Minaretten unter blauem Himmel"></div>
    <h2 class="audience__title serif">Meine Angebote richten<br>sich an:</h2>
    <div class="rule"></div>
    <div class="group">
      <p class="theme__head"><span class="num">1</span>Lehrkräfte allgemein:</p>
      <ul class="ticks"><li>Gewinnen Sie fundiertes Wissen, um <b>Schüler*innen unterschiedlicher Herkunft</b> besser zu begleiten</li></ul>
    </div>
    <div class="group">
      <p class="theme__head"><span class="num">2</span>Religionslehrerinnen und Religionslehrer:</p>
      <ul class="ticks"><li>Vertiefen Sie Ihr Wissen zu Inhalten der großen Religionen – praxisnah und aktuell!</li></ul>
    </div>
    <div class="group">
      <p class="theme__head"><span class="num">3</span>Fachkräfte im interkulturellen Kontext (Ausländerbehörde, Asylberatung, Gesundheitswesen)</p>
      <ul class="ticks"><li>Gewinnen Sie Sicherheit im Umgang mit religiös geprägten Verhaltensweisen!</li></ul>
    </div>
    <div class="group">
      <p class="theme__head"><span class="num">4</span>Reisefreudige &amp; Neugierige:</p>
      <ul class="ticks"><li>Entdecken Sie spannende Einblicke in Rituale, Werte und Feiertage weltweit!</li></ul>
    </div>
    <div class="audience__foot"></div>
  </div>
</section>

</body>
</html>
```